KMT Compliant Dietary Supplement Label for Nutritional Company

We are in need of a label for our line of 20+ dietary supplements that are specifically formulated to balance body chemistry and match the biochemical individuality of our users based on hair tissue mineral analysis.

We have a line of approximately 20 different dietary supplements that will require use of new label in both a small (90 capsule) and large (180 capsule) size. We will start with the initial label in which Product name, Supplement Facts, and Ingredient list will need to be modified for each particular product thereafter.

The label will be placed on a transparent blue bottle with the color of lid being decided after label design. We are open to a transparent light amber bottle with black lid but blue is our preference.

We would like the majority of the label to be blue. Solid blue, fading of blue to darker blue/black, or subtle background designs are welcome with involvement of white and hints of orange. We do not want pictorial images on the label.

Label size:
Small bottle (120cc): Label size ~ 2.25” x 5.875”
Large bottle (200cc): Label size ~ 2.75” x 7.625”

Front:
-Logo near top of label with product name and description in middle and capsule count near the bottom

Right Side:
-Supplement Facts: See current product image below in brief
-Ingredient list: See current product image below in brief
-Manufactured for: See image below (This is on the left side of our current bottle and would like it moved to the bottom of the right side)

Left side:
-Suggested use: See current product image below in brief
-Leave room for possible warning statement
-Leave room for possible lot number printing
-Keep out of the reach of children.

The first files below are our current supplement label with product information. This information is what is needed on the label and will likely need some adjustments as we are updating our line of supplements and changes in KMT requirements.

The following files are the logo files and color palette.

The remaining files are some designs we came across for inspiration.

Thank you.

Target Market(s)

Health Care Profressionals

Industry/Entity Type

Health Care and Nutrition

Requirements
Nice to have
• Product name needs to be on same line in all one color
Should not have
• Pictorial Images

```html
<!DOCTYPE html>
<html lang="en">
<head>
<meta charset="utf-8">
<title>Orvela Labs – Dietary Supplements Label</title>
<link href="https://fonts.googleapis.com/css2?family=Barlow+Condensed:wght@500;600&family=Barlow:wght@500&family=Montserrat:wght@500&display=swap" rel="stylesheet">
<style>
  :root {
    --canvas-bg: #ececec;
    --label-white: #f7f7f7;
    --navy: #1c2a4c;
    --navy-deep: #111a36;
    --navy-light: #34456c;
    --ink: #1f2a44;
    --orange: #e07b2a;
    --brand-blue: #3f6cb0;
  }
  * { margin: 0; padding: 0; box-sizing: border-box; }
  html, body { width: 1200px; height: 900px; overflow: hidden; }
  body { background: var(--canvas-bg); position: relative; }

  .label {
    position: absolute; left: 290px; top: 105px;
    width: 620px; height: 690px;
    background: var(--label-white);
    overflow: hidden;
    box-shadow: 0 2px 12px rgba(0,0,0,.08);
  }
  .navy-panel {
    position: absolute; left: 47px; right: 40px; top: 362px; bottom: 0;
    background: linear-gradient(160deg, var(--navy-light) 0%, var(--navy) 45%, var(--navy-deep) 100%);
  }
  .title-tab {
    position: absolute; left: 68px; right: 61px; top: 300px; height: 136px;
    background: var(--label-white);
    border-radius: 0 0 42px 42px;
  }

  .brand {
    position: absolute; left: 0; right: 0; top: 180px;
    display: flex; justify-content: center; align-items: center; gap: 14px;
  }
  .brand-dot { width: 20px; height: 20px; border-radius: 50%; background: var(--brand-blue); }
  .brand-name {
    font-family: "Montserrat", sans-serif; font-weight: 500;
    font-size: 46px; letter-spacing: 2px; color: var(--brand-blue);
  }

  .category {
    position: absolute; left: 0; right: 0; top: 272px;
    display: flex; justify-content: center; align-items: center; gap: 14px;
  }
  .category-bar {
    width: 89px; height: 20px;
    background: linear-gradient(90deg, var(--navy) 0%, var(--navy) 30%, var(--orange) 100%);
  }
  .category-bar.right { background: linear-gradient(90deg, var(--orange) 0%, var(--navy) 70%, var(--navy) 100%); }
  .category-text {
    font-family: "Barlow Condensed", sans-serif; font-weight: 600;
    font-size: 32px; color: var(--ink); line-height: 1;
  }

  .product-name {
    position: absolute; left: 0; right: 0; top: 298px; text-align: center;
    font-family: "Barlow Condensed", sans-serif; font-weight: 600;
    font-size: 90px; line-height: 1; color: var(--ink); letter-spacing: -0.5px;
  }
  .tagline {
    position: absolute; left: 0; right: 0; top: 387px; text-align: center;
    font-family: "Barlow", sans-serif; font-weight: 500;
    font-size: 24px; line-height: 30px; letter-spacing: 7px; color: var(--orange);
  }

  .dose-tag {
    position: absolute; left: 68px; top: 544px; width: 152px; height: 46px;
    background: linear-gradient(90deg, rgba(224,123,42,0) 0%, rgba(224,123,42,.55) 35%, var(--orange) 75%);
    border-radius: 0 4px 4px 0;
    padding: 5px 0 0 61px;
    font-family: "Barlow Condensed", sans-serif; font-weight: 500;
    font-size: 16px; line-height: 19px; color: var(--navy);
  }

  .capsule-seal { position: absolute; left: 362px; top: 462px; width: 120px; height: 120px; }
  .seal-ring { fill: none; stroke: #ffffff; stroke-width: 1.2; }
  .seal-arc { font-family: "Barlow Condensed", sans-serif; font-weight: 500; font-size: 11.5px; fill: #ffffff; letter-spacing: .6px; }
  .seal-count { font-family: "Barlow Condensed", sans-serif; font-weight: 500; font-size: 38px; fill: #ffffff; }
  .seal-unit { font-family: "Barlow Condensed", sans-serif; font-weight: 500; font-size: 15px; fill: #ffffff; }
</style>
</head>
<body>
  <main class="label">
    <div class="navy-panel"></div>
    <div class="title-tab"></div>

    <div class="brand">
      <span class="brand-dot"></span>
      <span class="brand-name">ORVELA LABS</span>
    </div>

    <div class="category">
      <span class="category-bar"></span>
      <span class="category-text">DIETARY</span>
      <span class="category-bar right"></span>
    </div>

    <h1 class="product-name">SUPPLEMENTS</h1>
    <p class="tagline">BALANCE BODY CHEMISTRY</p>

    <div class="dose-tag">750 MG<br>PER CAPSULE</div>

    <svg class="capsule-seal" viewBox="0 0 120 120" aria-label="180 capsules">
      <defs>
        <path id="seal-top" d="M 16 60 A 44 44 0 0 1 104 60"/>
        <path id="seal-bottom" d="M 12 60 A 48 48 0 0 0 108 60"/>
      </defs>
      <circle class="seal-ring" cx="60" cy="60" r="56"/>
      <circle class="seal-ring" cx="60" cy="60" r="38"/>
      <text class="seal-arc"><textPath href="#seal-top" startOffset="50%" text-anchor="middle">DIETARY SUPPLEMENTS</textPath></text>
      <text class="seal-arc"><textPath href="#seal-bottom" startOffset="50%" text-anchor="middle">BALANCE BODY CHEMISTRY</textPath></text>
      <text class="seal-arc" x="8" y="64">★</text>
      <text class="seal-arc" x="104" y="64">★</text>
      <text class="seal-count" x="60" y="64" text-anchor="middle">180</text>
      <text class="seal-unit" x="60" y="82" text-anchor="middle">CAPSULES</text>
    </svg>
  </main>
</body>
</html>
```